Building sign design

We need a sign design for the front of our automotive workshop building. The sign needs to fit the colours of our building and company. (black, red, grey and white). The sign needs to stand out and be a modern.

Sign is to replace the red Pennock Cells sign. 2900mmx2900mm.
Company logo attached (Highgear).
Also photos of old sign and building.

Sign needs to feature Highgear logo at top and what we do below.

-Warrant of Fitness
-Vehicle Servicing
-All Mechanical Repairs
-Tyres & Wheel Alignments
-Batteries & Diagnostics
-Automotive Parts
-Vehicle Sales.

Also needs a large "WOF" somewhere on sign.

And contact details at bottom of sign.
48 Tamsin Road
07 542 3917

```html
<!DOCTYPE html>
<html lang="en">
<head>
<meta charset="utf-8">
<title>Highgear – Workshop Building Sign</title>
<link rel="stylesheet" href="https://fonts.googleapis.com/css2?family=Archivo:wght@600;700;800;900&display=swap">
<style>
  :root {
    --sign-black: #050505;
    --sign-red: #e3141f;
    --sign-white: #ffffff;
    --sign-grey: #8d8d8d;
    --sign-dark-grey: #3a3a3a;
    --backdrop: #bdbdbd;
    --backdrop-edge: #7a7a7a;
  }
  html, body {
    margin: 0;
    padding: 0;
    width: 1200px;
    height: 2611px;
    overflow: hidden;
  }
  body {
    background: radial-gradient(ellipse at center, var(--backdrop) 0%, var(--backdrop-edge) 100%);
    font-family: "Archivo", Arial, sans-serif;
  }
  .building-sign {
    position: absolute;
    left: 50px;
    top: 755px;
    width: 1100px;
    height: 1100px;
    box-shadow: 0 20px 50px rgba(0,0,0,0.45);
  }
  .building-sign svg { display: block; width: 100%; height: 100%; }
  .brand-name { font-family: "Archivo", Arial, sans-serif; font-weight: 900; fill: var(--sign-red); }
  .service-label { font-family: "Archivo", Arial, sans-serif; font-weight: 700; font-size: 28px; fill: var(--sign-white); }
  .badge-text { font-family: "Archivo", Arial, sans-serif; font-weight: 900; font-size: 27px; fill: var(--sign-white); }
  .phone-number { font-family: "Archivo", Arial, sans-serif; font-weight: 900; font-size: 84px; fill: var(--sign-red); }
  .contact-line { font-family: "Archivo", Arial, sans-serif; font-weight: 800; font-size: 28px; fill: var(--sign-white); }
  .icon-line { fill: none; stroke: var(--sign-white); stroke-width: 2.4; stroke-linecap: round; stroke-linejoin: round; }
</style>
</head>
<body>
<main class="building-sign">
  <svg viewBox="0 0 912 912" xmlns="http://www.w3.org/2000/svg" aria-label="Highgear workshop sign">
    <defs>
      <linearGradient id="streak-grey" x1="0" y1="0" x2="1" y2="0">
        <stop offset="0" stop-color="#ffffff"/>
        <stop offset="1" stop-color="#6e6e6e"/>
      </linearGradient>
      <g id="service-hex">
        <polygon points="0,-55 48,-28 48,28 0,55 -48,28 -48,-28" fill="none" stroke="#9a9a9a" stroke-width="1.5"/>
        <polygon points="0,-50 43,-25 43,25 0,50 -43,25 -43,-25" fill="var(--sign-red)"/>
      </g>
    </defs>

    <!-- Panel -->
    <rect class="sign-panel" width="912" height="912" fill="var(--sign-black)"/>

    <!-- Brand name -->
    <text class="brand-name" x="456" y="128" text-anchor="middle" font-size="96" textLength="730" lengthAdjust="spacingAndGlyphs">HIGHGEAR</text>

    <!-- Services: left column -->
    <g class="service" transform="translate(146,265)">
      <use href="#service-hex"/>
      <text class="badge-text" x="0" y="10" text-anchor="middle">WOF</text>
    </g>
    <text class="service-label" x="214" y="261">WARRANT OF</text>
    <text class="service-label" x="214" y="294">FITNESS</text>

    <g class="service" transform="translate(146,385)">
      <use href="#service-hex"/>
      <g class="icon-line">
        <circle cx="-4" cy="4" r="9"/><circle cx="-4" cy="4" r="3.5"/>
        <rect x="-6" y="-22" width="26" height="14" rx="2"/>
        <path d="M6 -4 h14 v14 h-8"/>
        <circle cx="-16" cy="-12" r="5"/>
      </g>
    </g>
    <text class="service-label" x="214" y="381">ALL MECHANICAL</text>
    <text class="service-label" x="214" y="414">REPAIRS</text>

    <g class="service" transform="translate(146,505)">
      <use href="#service-hex"/>
      <g class="icon-line">
        <rect x="-22" y="-14" width="44" height="30" rx="2"/>
        <rect x="-16" y="-20" width="8" height="6"/><rect x="8" y="-20" width="8" height="6"/>
        <rect x="-15" y="-7" width="30" height="16"/>
        <path d="M2 -5 l-6 8 h6 l-4 7"/>
      </g>
    </g>
    <text class="service-label" x="214" y="501">BATTERIES &amp;</text>
    <text class="service-label" x="214" y="534">DIAGNOSTICS</text>

    <g class="service" transform="translate(146,625)">
      <use href="#service-hex"/>
      <g class="icon-line">
        <rect x="-13" y="-24" width="26" height="10" rx="1"/>
        <path d="M-18 4 l5 -12 h26 l5 12"/>
        <rect x="-22" y="4" width="44" height="14" rx="3"/>
        <circle cx="-13" cy="11" r="3"/><circle cx="13" cy="11" r="3"/>
        <path d="M-18 18 v5 M18 18 v5"/>
      </g>
      <text x="0" y="-16" text-anchor="middle" font-family="Archivo, Arial, sans-serif" font-weight="700" font-size="8" fill="#fff">SALE</text>
    </g>
    <text class="service-label" x="214" y="621">VEHICLE</text>
    <text class="service-label" x="214" y="654">SALES</text>

    <!-- Services: right column -->
    <g class="service" transform="translate(543,265)">
      <use href="#service-hex"/>
      <g class="icon-line">
        <path d="M-18 -18 l30 30 m0 0 l6 6"/>
        <circle cx="16" cy="16" r="5"/>
        <path d="M18 -18 l-30 30"/>
        <circle cx="-16" cy="16" r="6"/>
        <path d="M12 -22 a8 8 0 1 0 10 10"/>
      </g>
    </g>
    <text class="service-label" x="611" y="261">VEHICLE</text>
    <text class="service-label" x="611" y="294">SERVICING</text>

    <g class="service" transform="translate(543,385)">
      <use href="#service-hex"/>
      <g class="icon-line">
        <circle r="24"/><circle r="16"/><circle r="5"/>
        <path d="M0 -16 v11 M0 5 v11 M-16 0 h11 M5 0 h11 M-11 -11 l7 7 M4 4 l7 7 M11 -11 l-7 7 M-4 4 l-7 7"/>
      </g>
    </g>
    <text class="service-label" x="611" y="381">TYRES &amp; WHEEL</text>
    <text class="service-label" x="611" y="414">ALIGNMENTS</text>

    <g class="service" transform="translate(543,505)">
      <use href="#service-hex"/>
      <g class="icon-line">
        <rect x="-6" y="-24" width="12" height="8"/>
        <rect x="-9" y="-16" width="18" height="20"/>
        <path d="M-4 4 v16 M4 4 v16 M0 20 v5"/>
        <rect x="-24" y="-4" width="9" height="14"/><path d="M-20 10 v10"/>
        <rect x="15" y="-4" width="9" height="14"/><path d="M20 10 v10"/>
      </g>
    </g>
    <text class="service-label" x="611" y="501">AUTOMOTIVE</text>
    <text class="service-label" x="611" y="534">PARTS</text>

    <!-- Decorative swooshes -->
    <polygon class="swoosh-grey" points="500,642 912,528 912,598" fill="url(#streak-grey)"/>
    <polygon class="swoosh-white" points="190,738 830,650 760,662" fill="url(#streak-grey)"/>
    <polygon class="band-dark" points="0,728 290,690 300,730 0,768" fill="var(--sign-dark-grey)"/>
    <polygon class="band-red" points="0,800 912,646 912,912 0,912" fill="var(--sign-red)"/>
    <polygon class="band-corner" points="640,912 912,866 912,912" fill="var(--sign-black)"/>

    <!-- Phone bar -->
    <polygon class="phone-bar" points="209,727 838,727 812,817 236,817" fill="var(--sign-white)"/>
    <polygon class="phone-tab" points="74,727 204,727 243,833 100,833" fill="var(--sign-black)"/>
    <polygon points="92,815 100,833 88,833" fill="var(--sign-white)"/>
    <g class="phone-icon" transform="translate(159,772)">
      <circle r="37" fill="none" stroke="var(--sign-red)" stroke-width="5"/>
      <path d="M-12 -18 l6 -3 l7 11 l-5 4 c2 7 6 11 12 14 l4 -5 l11 7 l-3 6 c-16 3 -34 -16 -32 -34 z" fill="var(--sign-red)"/>
    </g>
    <text class="phone-number" x="255" y="803" textLength="525" lengthAdjust="spacingAndGlyphs">07 542 3917</text>

    <!-- Address and web -->
    <g class="pin-icon" transform="translate(97,856)" fill="none" stroke="var(--sign-white)" stroke-width="2.4">
      <circle cx="0" cy="-8" r="6"/>
      <path d="M0 -2 v12 M-7 10 h14"/>
    </g>
    <text class="contact-line" x="120" y="866">48 Tamsin Road</text>
    <rect x="364" y="842" width="2.5" height="28" fill="var(--sign-white)"/>
    <g class="globe-icon" transform="translate(398,856)" fill="none" stroke="var(--sign-white)" stroke-width="2">
      <circle r="11"/><ellipse rx="5" ry="11"/><path d="M-11 0 h22 M-9 -6 h18 M-9 6 h18"/>
    </g>
    <text class="contact-line" x="423" y="866" textLength="414" lengthAdjust="spacingAndGlyphs">highgearautomotive.co.nz</text>
  </svg>
</main>
</body>
</html>
```